Print & digital package needed for technology firm

We need a package of coordinating marketing materials for our technology business. We offer technology solutions to midsized organizations, including data center, outsourced IT, and technology consulting. Find more information on our website, www.pexlora.com. Design is the main concern, we can modify the text ongoing to best reflect our company’s offerings. The design should communicate technology expertise and strategic thinking. Our website is currently being updated with a “flat design” theme and we’d like design of these items to be flat, fresh, modern, and professional, without being boring.
Please use attached logo - can send in .ai/.eps/.psd/etc. Fonts in logo are Futura, Futura Book, and Lato. Please use pexLORA blue, #0372bb.
Please find attached one of our product flyers for one of the computers we lease. Fonts used are Roboto Slab (partial to this font) & Lato. Also attached copy of our business card design.
Taglines we have used include “Does IT hear what troubles you?” and “IT made simple” although we are open to new ideas.
Would like final products to be available in editable files - .psd/.tif/.ai/etc.

- 1 PowerPoint template
- 1 leaderboard ad (digital, 72dpi)
- 1 medium rectangle ad 300x250 (digital, 72dpi)
- 1 full page ad 8x11 (print, 300dpi)
- 1 half-page ad horizontal (print, 300dpi)
- 1 letterhead template
- 1 proposal front-page

There is potential for further graphic/print design opportunities for our business as well.

All, thank you for your assistance in understanding the budget process with this type of design contest - we have updated the project's budget to reflect the items we are requesting.

Please email mvarga at pexlora.com with inquiries or comments. Thank you.

Designers,

Due to an oversight, our project was listed as "refundable" - this has been corrected and changed to committed payment.
To enter into this contest, please pick 2-3 items from the list of desired materials (ads, powerpoint, letterhead, etc.) It is not necessary to submit all items which will be part of the final package to be considered for the contest.

Thank you. Please contact mvarga@pexlora.com for questions.
Best,
Mimi

CEOs, CFOs, CIOs, COOs - college+ educated, 30-60, professional.

```html
<!DOCTYPE html>
<html lang="en">
<head>
<meta charset="utf-8">
<title>pexLORA – Full Page Ad</title>
<link rel="stylesheet" href="https://fonts.googleapis.com/css2?family=Lato:ital,wght@0,300;0,400;0,700;0,900;1,700;1,900&family=Oswald:wght@700&display=swap">
<style>
  :root {
    --brand-blue: #0372bb;
    --brand-blue-deep: #035d9a;
    --brand-blue-soft: #4ea6e4;
    --ink: #2d3540;
    --paper: #ffffff;
    --paper-shade: #e4e8ed;
    --alert-red: #e0262a;
  }
  * { margin: 0; padding: 0; box-sizing: border-box; }
  html, body { width: 873px; height: 1200px; overflow: hidden; }
  body { font-family: "Lato", Arial, sans-serif; background: var(--paper); }

  .ad {
    position: relative;
    width: 873px;
    height: 1200px;
    overflow: hidden;
    background: linear-gradient(180deg, #ffffff 0%, #f2f5f8 35%, var(--paper-shade) 100%);
  }

  .question-banner {
    position: absolute;
    left: 0; top: 92px;
    width: 804px; height: 152px;
    background: var(--brand-blue);
  }
  .question-banner__text {
    position: absolute;
    left: 30px; top: 50%;
    transform: translateY(-50%);
    color: var(--paper);
    font-weight: 300;
    font-size: 39px;
    letter-spacing: -0.4px;
    white-space: nowrap;
  }
  .question-banner__text em {
    font-style: italic;
    font-weight: 900;
  }
  .question-banner__tail {
    position: absolute;
    left: 766px; top: 244px;
  }

  .brand {
    position: absolute;
    right: 68px; top: 294px;
    text-align: right;
  }
  .brand__name {
    display: block;
    color: var(--brand-blue);
    font-weight: 900;
    font-size: 78px;
    line-height: 1;
    letter-spacing: -1px;
  }
  .brand__tagline {
    display: block;
    margin-top: 2px;
    color: var(--ink);
    font-size: 18px;
    font-weight: 400;
  }

  .headline {
    position: absolute;
    right: 41px; top: 452px;
    text-align: right;
    color: var(--brand-blue);
    font-weight: 300;
    font-size: 92px;
    line-height: 112px;
    letter-spacing: -1px;
    white-space: nowrap;
  }

  .photo {
    position: absolute;
    left: 0; top: 740px;
    width: 873px; height: 328px;
    background:
      linear-gradient(180deg, rgba(228,232,237,0.9) 0%, rgba(228,232,237,0) 22%),
      linear-gradient(100deg, #f8f9fb 0%, #e6e9ed 30%, #9aa2ab 47%, #d7dce2 60%, #eef1f4 80%, #cfd5dc 100%);
  }

  .footer {
    position: absolute;
    left: 0; top: 1068px;
    width: 873px; height: 132px;
    background: var(--brand-blue);
  }
  .footer__call {
    position: absolute;
    right: 651px; top: 32px;
    text-align: right;
    color: var(--paper);
    font-style: italic;
    font-weight: 700;
    white-space: nowrap;
  }
  .footer__call-label { display: block; font-size: 24px; line-height: 30px; }
  .footer__phone { display: block; font-size: 29px; line-height: 36px; }
  .footer__divider {
    position: absolute;
    left: 238px; top: 36px;
    width: 1px; height: 62px;
    background: rgba(255,255,255,0.55);
  }
  .footer__info {
    position: absolute;
    left: 249px; top: 34px;
    white-space: nowrap;
  }
  .footer__web { display: block; color: var(--paper); font-size: 16px; line-height: 22px; }
  .footer__about { display: block; color: var(--brand-blue-soft); font-size: 15px; line-height: 21px; }
  .footer__social {
    position: absolute;
    left: 598px; top: 82px;
    display: flex; gap: 14px;
  }
  .footer__social span {
    width: 14px; height: 14px;
    border-radius: 50%;
    background: var(--brand-blue-soft);
  }

  .help-corner {
    position: absolute;
    left: 640px; top: 1022px;
  }
  .help-corner__label {
    position: absolute;
    right: 10px; bottom: 18px;
    color: var(--paper);
    font-family: "Oswald", "Arial Narrow", sans-serif;
    font-weight: 700;
    font-size: 56px;
    line-height: 1;
  }
</style>
</head>
<body>
<main class="ad">
  <header class="question-banner">
    <p class="question-banner__text">Is IT solving your problems, <em>or creating them?</em></p>
  </header>
  <svg class="question-banner__tail" width="38" height="38" viewBox="0 0 38 38" aria-hidden="true">
    <polygon points="0,0 38,0 0,38" fill="var(--brand-blue-deep)"/>
  </svg>

  <div class="brand">
    <span class="brand__name">pexLORA</span>
    <span class="brand__tagline">IT made simple!</span>
  </div>

  <h1 class="headline">Don’t operate<br>without an IT plan.</h1>

  <div class="photo" role="img" aria-label="Photo of a frustrated businessman in a white shirt slumped with his head on a white desk beside an open laptop"></div>

  <footer class="footer">
    <p class="footer__call">
      <span class="footer__call-label">Call us today!</span>
      <span class="footer__phone">555-014-2273</span>
    </p>
    <div class="footer__divider"></div>
    <p class="footer__info">
      <span class="footer__web">www.pexlora.com</span>
      <span class="footer__about">Since 1979, we have been providing expert<br>technology solutions to associations.</span>
    </p>
    <div class="footer__social" aria-hidden="true"><span></span><span></span><span></span></div>
  </footer>

  <div class="help-corner">
    <svg width="233" height="178" viewBox="0 0 233 178" aria-hidden="true">
      <defs>
        <linearGradient id="helpBlue" x1="0" y1="0" x2="1" y2="1">
          <stop offset="0" stop-color="#1b8ae0"/>
          <stop offset="1" stop-color="var(--brand-blue)"/>
        </linearGradient>
        <linearGradient id="helpRed" x1="0" y1="1" x2="1" y2="0">
          <stop offset="0" stop-color="#c8171c"/>
          <stop offset="1" stop-color="var(--alert-red)"/>
        </linearGradient>
      </defs>
      <polygon points="12,46 55,0 55,178 0,178" fill="#023f6b" opacity="0.55"/>
      <polygon points="55,0 233,0 55,178" fill="url(#helpBlue)"/>
      <polygon points="233,0 233,178 55,178" fill="url(#helpRed)"/>
    </svg>
    <span class="help-corner__label">HELP</span>
  </div>
</main>
</body>
</html>
```